Business card design for engineering firm specializing in defense industry.

We need a professional business card design. Something simple but stands out. We are an engineering company specializing in composites in the defense industry.
Industry/Entity Type
Defense
Contact Information for Business Card
A simple black business card with the Varlonix yellow color is what we had in mind but open for other designs.
Colors
ffc214

```html
<!DOCTYPE html>
<html lang="en">
<head>
<meta charset="utf-8">
<title>Varlonix Business Card</title>
<link href="https://fonts.googleapis.com/css2?family=Lato:wght@400;700;900&display=swap" rel="stylesheet">
<style>
  :root {
    --page: #151515;
    --card: #232323;
    --card-light: #2e2e2e;
    --accent: #ffc214;
    --text: #f2f2f2;
    --muted: #cfcfcf;
  }
  * { margin: 0; padding: 0; box-sizing: border-box; }
  html, body { width: 1200px; height: 912px; overflow: hidden; }
  body {
    background: var(--page);
    font-family: "Lato", Arial, sans-serif;
    color: var(--text);
    position: relative;
  }
  .card {
    position: absolute;
    width: 700px;
    height: 400px;
    background: var(--card);
    box-shadow: 0 18px 40px rgba(0,0,0,.55);
    overflow: hidden;
  }
  .card-front { left: 60px; top: 40px; }
  .card-back { left: 440px; top: 472px; }

  .front-backdrop {
    position: absolute; inset: 0;
    background: radial-gradient(ellipse at 50% 45%, var(--card-light) 0%, var(--card) 55%, #1d1d1d 100%);
  }
  .wordmark {
    display: flex; align-items: center; gap: 14px;
    font-weight: 900; color: var(--text); letter-spacing: .5px;
  }
  .wordmark-square { background: var(--accent); flex: none; }
  .front-wordmark {
    position: absolute; left: 50%; top: 150px; transform: translateX(-50%);
    font-size: 64px;
  }
  .front-wordmark .wordmark-square { width: 40px; height: 40px; }
  .front-url {
    position: absolute; left: 0; right: 0; top: 300px;
    text-align: center; font-size: 17px; color: var(--text); letter-spacing: .3px;
  }

  .back-wordmark {
    position: absolute; left: 60px; top: 150px; font-size: 44px;
  }
  .back-wordmark .wordmark-square { width: 28px; height: 28px; }
  .divider {
    position: absolute; left: 372px; top: 60px; width: 2px; height: 190px;
    background: var(--accent);
  }
  .contact { position: absolute; left: 404px; top: 58px; }
  .contact-name { color: var(--accent); font-weight: 700; font-size: 25px; }
  .contact-role { font-size: 15px; color: var(--muted); margin-top: 2px; margin-bottom: 16px; }
  .contact-list { list-style: none; }
  .contact-item {
    display: flex; align-items: center; gap: 12px;
    font-size: 15px; line-height: 26px; color: var(--text);
  }
  .contact-item svg { width: 15px; height: 15px; fill: var(--accent); flex: none; }
  .address {
    position: absolute; left: 0; right: 0; bottom: 46px;
    text-align: center; font-size: 19px; color: var(--text); letter-spacing: .3px;
  }
  .accent-band {
    position: absolute; left: 0; right: 0; bottom: 0; height: 10px;
    background: var(--accent);
  }
</style>
</head>
<body>

  <section class="card card-front">
    <div class="front-backdrop" role="img" aria-label="Dark faceted geometric panels radiating from the centre"></div>
    <div class="wordmark front-wordmark">
      <span class="wordmark-square"></span>
      <span>Varlonix</span>
    </div>
    <p class="front-url">www.varlonixinc.com</p>
  </section>

  <section class="card card-back">
    <div class="wordmark back-wordmark">
      <span class="wordmark-square"></span>
      <span>Varlonix</span>
    </div>
    <div class="divider"></div>
    <div class="contact">
      <h1 class="contact-name">Daniel Hartwell</h1>
      <p class="contact-role">Manager</p>
      <ul class="contact-list">
        <li class="contact-item">
          <svg viewBox="0 0 16 16" aria-hidden="true"><path d="M3.5 1 6 3.5 4.7 5.6c.9 2 2.6 3.8 4.7 4.7L11.5 9 15 11.5 13.5 14.8C7 14.8 1.2 9 1.2 2.5z"/></svg>
          <span>512 555 0142</span>
        </li>
        <li class="contact-item">
          <svg viewBox="0 0 16 16" aria-hidden="true"><path d="M4 1h7l1 1v3H4zM1 6h14v6h-3v3H4v-3H1zm4 4v3.5h6V10z"/></svg>
          <span>512 555 0143</span>
        </li>
        <li class="contact-item">
          <svg viewBox="0 0 16 16" aria-hidden="true"><path d="M1 3h14v10H1zm1.5 1.5v.3L8 9l5.5-4.2v-.3z"/></svg>
          <span>info@varlonixinc.com</span>
        </li>
        <li class="contact-item">
          <svg viewBox="0 0 16 16" aria-hidden="true"><path d="M8 1a7 7 0 1 0 0 14A7 7 0 0 0 8 1zm0 1.5c.8 0 1.7 1.7 2 4.5H6c.3-2.8 1.2-4.5 2-4.5zM2.6 7h2c0-1.6.3-3 .8-4A5.5 5.5 0 0 0 2.6 7zm8.8 0h2a5.5 5.5 0 0 0-2.8-4c.5 1 .8 2.4.8 4zM2.6 9a5.5 5.5 0 0 0 2.8 4c-.5-1-.8-2.4-.8-4zm3.4 0c.3 2.8 1.2 4.5 2 4.5s1.7-1.7 2-4.5zm5.4 0c0 1.6-.3 3-.8 4a5.5 5.5 0 0 0 2.8-4z"/></svg>
          <span>www.varlonixinc.com</span>
        </li>
      </ul>
    </div>
    <p class="address">28 Harlow Avenue, Bangor, Maine 04401</p>
    <div class="accent-band"></div>
  </section>

</body>
</html>
```